Responsive, beautiful email sign-up process pages

My client wants to re-imagine their email newsletter sign up process. The funnel currently starts in the first panel of their home page carousel at:

https://thriftbeacon.co.uk/

It is also featured in the right side of the footer.

I would like to start, what could become a full template re-design project by optimising this crucial user journey. I am attaching the screenshots from the current user journey below and it would be great to get some designs that improve on the look and feel.

Thank you,
Dorian

Target Market(s)

People who want to maximise the interest rate they receive on their cash savings.

Industry/Entity Type

Financial Service

Coding

Coded - Design and coding required

Number of Pages Required

4 page

Font styles to use
Sans Serif

Requirements
Must have
• A well designed, responsive design for all of the elements of the user journey funnel that works well on desktop, laptop, tablet and phone. The site is currently using Bootstrap 3.* for the responsive templates, so it would be useful to continue leveraging these libraries, but in a much more visually appealing way.
• It is felt that the current overall site is dull and unprofessional, so we are using this as a way of showing how much better it could be, which should lead to a sitewide "facelift".
Nice to have
• Creative use of css, svg and javascript to optimise the user experience on all target platforms.
Should not have
• Non-responsive designs.

```html
<!DOCTYPE html>
<html lang="en">
<head>
<meta charset="utf-8">
<title>Thrift Beacon – Free Savings Information Sign-up</title>
<link href="https://fonts.googleapis.com/css2?family=Open+Sans:wght@400;600;700&display=swap" rel="stylesheet">
<style>
:root{
  --orange:#ef7a1a;
  --orange-dark:#d9660c;
  --charcoal:#333638;
  --bar:#252729;
  --text:#555;
  --muted:#8a8a8a;
  --line:#dcdcdc;
  --paper:#ffffff;
  --mist:#ececec;
  --panel:rgba(28,30,32,.78);
}
*{box-sizing:border-box;margin:0;padding:0}
html,body{width:804px;height:1200px;overflow:hidden}
body{font-family:"Open Sans",Arial,sans-serif;color:var(--text);background:var(--mist);font-size:10px}
.page{width:804px;background:var(--paper)}

.topbar{height:28px;background:var(--bar);display:flex;align-items:center;justify-content:space-between;padding:0 34px}
.social{display:flex;gap:6px}
.social span{width:13px;height:13px;border-radius:50%;background:var(--orange);display:block}
.account{display:flex;gap:3px}
.account a{background:var(--orange);color:#fff;text-decoration:none;font-size:8.5px;padding:4px 10px;white-space:nowrap}

.header{height:78px;display:flex;align-items:center;justify-content:space-between;padding:0 34px}
.brand{display:flex;align-items:center;gap:8px}
.brand-dot{width:30px;height:30px;border-radius:50%;background:var(--orange)}
.brand-name{font-size:20px;font-weight:700;color:var(--charcoal);line-height:1}
.contact{display:flex;align-items:center;gap:8px}
.contact-text{font-size:10px;color:var(--charcoal);line-height:1.3}
.contact-text strong{display:block;font-size:14px;color:var(--orange)}

.nav{height:28px;background:var(--charcoal);display:flex;padding:0 34px}
.nav a{color:#fff;text-decoration:none;font-size:8.5px;padding:0 9.5px;display:flex;align-items:center;border-right:1px solid #474a4c;white-space:nowrap}
.nav a.active{background:var(--orange)}

.hero{position:relative;height:420px}
.hero-photo{position:absolute;inset:0;background:linear-gradient(100deg,#6d7d5a 0%,#a9b98a 35%,#d9c9b0 60%,#8fa771 100%)}
.hero-tabs{position:absolute;top:8px;left:34px;display:flex;gap:4px}
.hero-tabs span{background:rgba(255,255,255,.94);color:var(--charcoal);font-size:9.5px;padding:6px 22px;white-space:nowrap}
.hero-tabs span.on{background:var(--charcoal);color:#fff}
.signup{position:absolute;left:34px;top:180px;width:260px;background:var(--panel);padding:16px 16px 18px;color:#fff}
.signup h1{font-size:21px;font-weight:600;line-height:1.25;margin-bottom:14px}
.signup h1 em{color:var(--orange);font-style:normal;font-weight:700}
.signup ul{list-style:none;font-size:9.5px;margin-bottom:14px}
.signup li{display:flex;align-items:center;gap:7px;margin-bottom:9px}
.signup li::before{content:"";width:6px;height:6px;border-radius:50%;background:#fff;flex:none}
.field{background:#fff;color:#999;font-size:9px;padding:8px 9px;margin-bottom:7px}
.cta{background:var(--orange);color:#fff;font-size:9px;font-weight:700;text-align:center;padding:9px 0}

.section-title{color:var(--orange);text-align:center;font-size:12px;font-weight:600;padding:20px 0 10px}
.advice{display:flex;gap:12px;padding:0 34px}
.advice-card{flex:1;border:1px solid var(--line)}
.advice-card h3{background:var(--charcoal);color:#fff;font-size:11px;font-weight:600;text-align:center;padding:7px 0}
.advice-card p{font-size:7.5px;color:var(--muted);text-align:center;padding:7px 10px 3px;line-height:1.4}
.advice-card a{display:block;text-align:center;font-size:7.5px;color:var(--orange);padding-bottom:7px;text-decoration:none}

.press{display:flex;gap:12px;padding:0 34px}
.quote{flex:1;border:1px solid var(--line);padding:8px 10px;font-size:7.5px;line-height:1.45;color:var(--muted)}
.quote cite{display:block;font-style:normal;font-weight:600;color:var(--charcoal);margin-top:4px}
.press-marks{display:flex;justify-content:space-between;padding:16px 34px 0}
.press-marks span{width:54px;height:20px;background:#cfcfcf}

.queries{text-align:center;font-size:13px;font-weight:600;color:var(--charcoal);padding:26px 0 16px}

.footer{background:var(--charcoal);height:218px;display:flex;gap:24px;padding:18px 34px;color:#bdbdbd;font-size:8px;line-height:1.5}
.footer h4{color:var(--orange);font-size:9.5px;font-weight:700;margin-bottom:7px}
.foot-about{width:190px}
.foot-about p{margin-bottom:7px}
.foot-links{flex:1}
.foot-links .cols{display:flex;gap:22px}
.foot-links ul{list-style:none}
.foot-links li{margin-bottom:4px}
.foot-news{width:200px}
.foot-news .field{margin:7px 0 5px}
.foot-news .cta{padding:6px 0}
.foot-social{display:flex;gap:5px;margin-top:10px}
.foot-social span{width:13px;height:13px;border-radius:50%;background:var(--orange)}

.legal{background:var(--bar);height:24px;display:flex;align-items:center;justify-content:space-between;padding:0 34px;color:#aaa;font-size:7.5px}
</style>
</head>
<body>
<div class="page">
  <div class="topbar">
    <div class="social"><span></span><span></span><span></span><span></span></div>
    <div class="account"><a href="#">Help</a><a href="#">Register Now</a><a href="#">Sign In</a></div>
  </div>

  <header class="header">
    <div class="brand"><span class="brand-dot"></span><span class="brand-name">thrift beacon</span></div>
    <div class="contact">
      <svg width="22" height="22" viewBox="0 0 24 24"><circle cx="12" cy="12" r="12" fill="#ef7a1a"/><path d="M8 6l2.5 0 1 3-1.5 1.2a7 7 0 0 0 3.8 3.8L15 12.5l3 1V16a2 2 0 0 1-2 2A10 10 0 0 1 6 8a2 2 0 0 1 2-2z" fill="#fff"/></svg>
      <div class="contact-text">Speak Direct to a Savings Expert<strong>0800 555 0142</strong></div>
    </div>
  </header>

  <nav class="nav">
    <a class="active" href="#">Home</a><a href="#">Concierge Service</a><a href="#">Best Buy Tables</a><a href="#">Rate Trackers</a><a href="#">News and Views</a><a href="#">Advice and Guides</a><a href="#">Favourites</a><a href="#">Promotions</a><a href="#">About Us</a><a href="#">Contact Us</a>
  </nav>

  <section class="hero">
    <div class="hero-photo" role="img" aria-label="Photo of a smiling mother holding her young daughter outdoors"></div>
    <div class="hero-tabs"><span class="on">FREE Information</span><span>Inheritance Tax</span><span>Over £100,000 in savings</span></div>
    <form class="signup">
      <h1>Get <em>FREE</em> whole of market information</h1>
      <ul>
        <li>Unconstrained Best Buy Tables</li>
        <li>Account Monitoring and Alert Services</li>
        <li>Access to Savings Experts</li>
      </ul>
      <div class="field">Enter your email address</div>
      <div class="cta">CHOOSE YOUR FREE SERVICES</div>
    </form>
  </section>

  <h2 class="section-title">Specialist Advice</h2>
  <div class="advice">
    <div class="advice-card"><h3>£100,000 plus in savings?</h3><p>Our experts can help you spread larger sums safely across the best paying accounts.</p><a href="#">Find out more about our service</a></div>
    <div class="advice-card"><h3>Wealth Management</h3><p>Independent guidance to help you plan, protect and grow your wealth over time.</p><a href="#">Find out more about our service</a></div>
    <div class="advice-card"><h3>Take Our £50 Challenge</h3><p>We will find you a better rate on your savings or we will give you fifty pounds.</p><a href="#">Find out more about the challenge</a></div>
  </div>

  <h2 class="section-title">Thrift Beacon in the Press</h2>
  <div class="press">
    <div class="quote">"Thrift Beacon is a trusted source of clear and honest savings information for everyone who wants a fairer return."<cite>Savings columnist, national daily</cite></div>
    <div class="quote">"An independent service that keeps track of rates so savers do not have to, flagging when a better deal appears."<cite>Personal finance editor, weekly paper</cite></div>
    <div class="quote">"One of the best ways to make sure your cash is working hard, with alerts whenever your rate falls."<cite>Money reporter, broadcast news</cite></div>
  </div>
  <div class="press-marks"><span></span><span></span><span></span><span></span><span></span><span></span><span></span><span></span><span></span><span></span></div>

  <p class="queries">Queries? Call us on 0800 555 0142</p>

  <footer class="footer">
    <div class="foot-about">
      <h4>We're working for a better deal for savers</h4>
      <p>Thrift Beacon monitors and advises on the whole of the savings market, with no commission bias.</p>
      <p>Read more about us</p>
    </div>
    <div class="foot-links">
      <h4>Your Savings Account</h4>
      <div class="cols">
        <ul><li>Best Buy Tables</li><li>Rate Trackers</li><li>Fixed Rate Bonds</li><li>Notice Accounts</li><li>Cash ISAs</li></ul>
        <ul><li>News and Views</li><li>Advice and Guides</li><li>Promotions</li><li>About Us</li><li>Contact Us</li></ul>
      </div>
    </div>
    <form class="foot-news">
      <h4>Sign up for our newsletter</h4>
      <p>Keep in the loop with the savings market, rate changes and our latest expert views.</p>
      <div class="field">Enter your email address</div>
      <div class="cta">Sign up</div>
      <div class="foot-social"><span></span><span></span><span></span><span></span></div>
    </form>
  </footer>
  <div class="legal"><span>Terms &amp; Conditions · Privacy Policy · Cookie Policy · Website Security</span><span>© Thrift Beacon</span></div>
</div>
</body>
</html>
```